Info about Getting Rid of Items That People No Longer Want or Need and Would Rather Have the Cash

We need a flyer made to pass out to potential customers describing what it is that we do. We would like for it to be a one page front and back flyer.
Our company helps people who are downsizing or getting rid of items that they no longer want and are unsure of their value. Most Millennials have no interest in their parents items--whether that be art, sterling flatware, jewelry, decorative items or collectibles. On top of that the market is slowing turning as there is more 'stuff" on the market than ever before and less buyers.
We have included some images as examples. For instance: a newspaper headline showing "Millennials Don't Want Your Stuff". In one of the small columns below there could be a picture of an Felix Dunmore painting with a caption reading "Man Buys Original Dunmore for $20 in Garage Sale". Or something like that.
We are open to suggestions and encourage your creativity. These are just examples of what we came up with. These issues, kids not wanting their parents stuff and worry about squandering something special because they didn't know what it is and what its worth are big concerns.
On the back page we are thinking about using a 5 step process to simplify what we do.
Below is a rough example of the 5 steps.
1) Schedule Free In-Home Visit
Please contact us to schedule an appointment
2) Questions, Answers and Facts
We will answer any questions you have and ask you enough questions to make sure we know what your goals are. We will also inform you about market trends and other information related to downsizing
3) The Tour and The Treasure Hunt
You will take us on a tour of your home and point out items you are selling. We will take pictures, notes and point out any treasures that you may not realize you have.
4) Research, Research, Research
We take our notes and photographs back to research your items. Then we will check with our network of experts, dealers and buyers across the country to determine the best market.
5) The Game Plan
We will go over our findings with you. Then we will discuss ways to sell the items to get the highest return.
We have also attached sample images of our business card. We will also want to include our contact information:
Gordon Pellham
555-382-9170
info@gordonapellham.example
www.gordonapellham.example
Target Market(s)
Elderly People or people downsizing
Industry/Entity Type
Cash
Font styles to use
Colors
Designer to choose colors to be used in the design.
Look and feel

```html
<!DOCTYPE html>
<html lang="en">
<head>
<meta charset="utf-8">
<title>Gordon A Pellham – Flyer Front and Back</title>
<link href="https://fonts.googleapis.com/css2?family=Roboto:wght@700;900&family=Roboto+Condensed:ital,wght@0,300;0,400;0,700;1,700&display=swap" rel="stylesheet">
<style>
  :root {
    --backdrop: #2e2119;
    --paper: #ffffff;
    --ink: #1b1b1b;
    --yellow: #ffc20e;
    --gold: #a0885a;
    --gold-text: #a8864a;
    --band-dark: #342b22;
    --footer-tan: #a8977a;
    --rule: #b39a62;
    --muted: #3b3b3b;
  }
  * { box-sizing: border-box; margin: 0; padding: 0; }
  html, body { width: 1200px; height: 1200px; overflow: hidden; }
  body {
    background: var(--backdrop);
    font-family: "Roboto Condensed", "Arial Narrow", sans-serif;
    color: var(--ink);
    position: relative;
  }
  .page {
    position: absolute;
    top: 240px;
    width: 560px;
    height: 720px;
    background: var(--paper);
    overflow: hidden;
  }
  .page--front { left: 26px; }
  .page--back { left: 614px; }

  /* ---------- front ---------- */
  .hero-photo {
    position: absolute; left: 0; top: 0; width: 560px; height: 317px;
    background: linear-gradient(180deg, #3d2414 0%, #6b3a1c 40%, #5a3118 70%, #2c1a10 100%);
  }
  .hero-title {
    position: absolute; left: 190px; top: 118px; width: 370px; text-align: center;
    font-family: "Roboto", sans-serif; font-weight: 700; font-size: 32px; color: #fff;
    text-shadow: 0 2px 4px rgba(0,0,0,.7); letter-spacing: .3px;
  }
  .hero-sub {
    position: absolute; left: 190px; top: 174px; width: 370px; text-align: center;
    font-family: "Roboto", sans-serif; font-weight: 700; font-size: 19px; line-height: 25px;
    color: #fff; text-shadow: 0 2px 4px rgba(0,0,0,.7);
  }
  .headline-box {
    position: absolute; left: 38px; top: 246px; width: 187px; height: 235px;
    background: var(--yellow); padding: 22px 0 0 22px;
    font-family: "Roboto", sans-serif; font-weight: 900; line-height: .92;
  }
  .headline-box::before {
    content: ""; position: absolute; left: 12px; top: 10px; right: 10px; bottom: 10px;
    border-right: 2px solid var(--ink); border-bottom: 2px solid var(--ink);
  }
  .headline-box::after {
    content: ""; position: absolute; left: 22px; bottom: -32px;
    border-left: 0 solid transparent; border-right: 34px solid transparent;
    border-top: 32px solid var(--yellow);
  }
  .headline-box span { display: block; }
  .hl-small { font-size: 29px; font-weight: 700; }
  .hl-big { font-size: 64px; letter-spacing: -1px; }
  .hl-mid { font-size: 33px; font-weight: 700; margin-top: 4px; }
  .intro {
    position: absolute; left: 241px; top: 330px; width: 305px;
  }
  .intro h2 {
    font-weight: 400; font-size: 18px; line-height: 19px; margin-bottom: 8px;
  }
  .intro p { font-size: 8.9px; line-height: 13px; margin-bottom: 10px; }
  .intro em { font-style: italic; font-weight: 700; }
  .collage {
    position: absolute; left: 0; top: 488px; width: 560px; height: 178px;
    background: linear-gradient(180deg, #ffffff 0%, #f1ece4 25%, #8a6a4a 60%, #4a3428 100%);
  }
  .painting-thumb {
    position: absolute; left: 337px; top: 512px; width: 52px; height: 50px;
    background: linear-gradient(135deg, #f2d23c 0%, #e88aa0 50%, #2fa4c8 100%);
  }
  .garage-caption {
    position: absolute; left: 396px; top: 505px; transform: rotate(-6deg); transform-origin: left top;
    color: var(--gold-text); font-weight: 700; line-height: 1.05;
  }
  .garage-caption .small { display: block; font-size: 10px; }
  .garage-caption .large { display: block; font-size: 17px; }
  .contact-bar {
    position: absolute; left: 0; bottom: 0; width: 560px; height: 54px;
    background: var(--footer-tan); color: #fff; font-weight: 700; font-size: 14.5px;
    display: flex; align-items: center; gap: 27px; padding: 0 0 10px 60px;
  }

  /* ---------- back ---------- */
  .back-band {
    position: absolute; left: 0; top: 0; width: 560px; height: 75px;
    background: var(--band-dark); display: flex; align-items: baseline; padding: 34px 0 0 45px; gap: 18px;
  }
  .back-band h1 {
    font-family: "Roboto", sans-serif; font-weight: 700; font-size: 27px; color: var(--gold-text);
  }
  .back-band p { font-size: 9px; color: #fff; letter-spacing: .1px; }
  .owner-photo {
    position: absolute; left: 47px; top: 92px; width: 86px; height: 103px;
    background: linear-gradient(180deg, #c9ccd0 0%, #9a8f86 50%, #2c2c34 100%);
  }
  .bio {
    position: absolute; left: 146px; top: 92px; width: 384px;
    font-size: 9.5px; line-height: 12.8px; text-align: justify; color: var(--muted);
  }
  .bio strong { display: block; margin-top: 8px; font-style: italic; font-weight: 700; color: var(--ink); text-align: left; }
  .process-title {
    position: absolute; left: 47px; top: 208px; font-size: 32px; font-weight: 300; color: var(--ink);
  }
  .process-title b { font-weight: 700; }
  .steps { position: absolute; left: 47px; top: 255px; width: 483px; list-style: none; }
  .step { position: absolute; left: 0; width: 483px; }
  .step-num {
    position: absolute; left: 0; width: 66px; height: 66px; border-radius: 50%;
    background: var(--gold); color: #fff; font-size: 29px; font-weight: 300;
    display: flex; align-items: center; justify-content: center;
  }
  .step-body {
    position: absolute; left: 80px; width: 403px; border-bottom: 1.5px solid var(--rule);
  }
  .step-body h3 { font-size: 14px; font-weight: 700; color: var(--gold-text); line-height: 16px; }
  .step-body p { font-size: 8.8px; line-height: 12px; color: var(--muted); }
  .step-body p.lead { font-size: 12px; line-height: 16px; color: var(--ink); }
  .cta {
    position: absolute; left: 48px; top: 634px; font-size: 23.5px; font-weight: 400; color: var(--ink);
  }
  .page--back .contact-bar { height: 53px; padding: 0 0 14px 48px; gap: 34px; border-top: 2px solid #6a5f4f; }
</style>
</head>
<body>

<section class="page page--front" aria-label="Flyer front">
  <div class="hero-photo" role="img" aria-label="Gordon A Pellham standing with arms crossed in front of wooden bookshelves"></div>
  <div class="hero-title">GORDON A PELLHAM</div>
  <div class="hero-sub">COLLECTIBLE ASSET BUYER<br>BROKER &amp; CONSULTANT</div>

  <div class="headline-box">
    <span class="hl-small">Millennials</span>
    <span class="hl-big">Don't</span>
    <span class="hl-mid">Want Your</span>
    <span class="hl-big">Stuff</span>
  </div>

  <div class="intro">
    <h2>Getting Rid of Items That People No Longer Want or Need and Would Rather Have the Cash</h2>
    <p>Our company helps people who are downsizing or getting rid of items that they no longer want and are unsure of their value. Most Millennials have no interest in their parents items–whether that be <em>ART, STERLING FLATWARE, JEWELRY, DECORATIVE ITEMS OR COLLECTIBLES.</em></p>
    <p>On top of that the market is slowing turning as there is more 'stuff" on the market than ever before and less buyers.</p>
  </div>

  <div class="collage" role="img" aria-label="Collage of collectibles: jeweled figurine, perfume bottle, coins, typewriter, camera, watch, flask, painting and rotary telephone"></div>
  <div class="painting-thumb" role="img" aria-label="Pop art portrait painting by Felix Dunmore"></div>
  <div class="garage-caption">
    <span class="small">Man Buys Original Dunmore for</span>
    <span class="large">$20 in Garage Sale</span>
  </div>

  <footer class="contact-bar">
    <span>555-382-9170</span>
    <span>info@gordonapellham.example</span>
    <span>www.gordonapellham.example</span>
  </footer>
</section>

<section class="page page--back" aria-label="Flyer back">
  <header class="back-band">
    <h1>GORDON A PELLHAM</h1>
    <p>COLLECTIBLE ASSET BUYER, BROKER &amp; CONSULTANT</p>
  </header>

  <div class="owner-photo" role="img" aria-label="Portrait of Gordon A Pellham in a suit"></div>
  <div class="bio">
    Over the last 15 years I have been able to help thousands of clients sell their items. During this time I have purchased millions of dollars worth of jewelry, coins, watches, sterling and collectibles. Throughout the years we have maintained an A+ rating with the Fair Trade Council and have never had a complaint. Over 95% of our business comes through referrals from prior customers and companies that serve the estate and senior industry including auction houses, realtors, senior communities and estate sale companies.
    <strong>We are proud of our reputation and work hard to grow our standing in the community.</strong>
  </div>

  <h2 class="process-title"><b>5 step</b> process to simplify what we do.</h2>

  <ol class="steps">
    <li class="step" style="top:0">
      <div class="step-num">1</div>
      <div class="step-body" style="top:12px;height:55px">
        <h3>Schedule Free In-Home Visit</h3>
        <p class="lead">Please contact us to schedule an appointment</p>
      </div>
    </li>
    <li class="step" style="top:74px">
      <div class="step-num">2</div>
      <div class="step-body" style="top:12px;height:58px">
        <h3>Questions, Answers and Facts</h3>
        <p>We will answer any questions you have and ask you enough questions to make sure we know what your goals are. We will also inform you about market trends and other information related to downsizing</p>
      </div>
    </li>
    <li class="step" style="top:147px">
      <div class="step-num">3</div>
      <div class="step-body" style="top:13px;height:56px">
        <h3>The Tour and The Treasure Hunt</h3>
        <p>You will take us on a tour of your home and point out items you are selling. We will take pictures, notes and point out any treasures that you may not realize you have.</p>
      </div>
    </li>
    <li class="step" style="top:220px">
      <div class="step-num">4</div>
      <div class="step-body" style="top:13px;height:57px">
        <h3>Research, Research, Research</h3>
        <p>We take our notes and photographs back to research your items. Then we will check with our network of experts, dealers and buyers across the country to determine the best market.</p>
      </div>
    </li>
    <li class="step" style="top:294px">
      <div class="step-num">5</div>
      <div class="step-body" style="top:13px;height:54px">
        <h3>The Game Plan</h3>
        <p>We will go over our findings with you.<br>Then we will discuss ways to sell the items to get the highest return</p>
      </div>
    </li>
  </ol>

  <p class="cta">CONTACT US TO SCHEDULE AN APPOINTMENT</p>

  <footer class="contact-bar">
    <span>555-382-9170</span>
    <span>info@gordonapellham.example</span>
    <span>www.gordonapellham.example</span>
  </footer>
</section>

</body>
</html>
```